Healthy juice company needs a branded shipping box

I am looking for a branded box that is 10"x10"x10" in standard brown. This is for the box we ship the juice in.

The box should serve as an advertising platform in itself. We offer a subscription juice service. People get a box of juice delivered every week.

The customer should see the box and feel good about what they ordered because it's something healthy they're doing for themselves. The imagery/wording should reinforce that they're doing something healthy for themselves.

Other people who see the box should be curious enough to look us up and want a box for themselves.

I'd like ONE color in the final print.

I'd like the 4 sides of the box to be printed.

The design is up to you.

Inspiration boxes: Maple Ladle, Tidy Skillet, PrintWren

Target Market(s)

Our customers subscribe to our juice because it helps them eat the fruits and veggies they normally wouldn't. They are typically 30-40yrs old, with families, and are upper middle class.

Industry/Entity Type

Delivery Service

Font styles to use
Sans Serif

Colors
f78f20
9bcb3c
ffffff

Requirements
Must have
• The design should feel clean, bright, happy, casual, and healthy.
• Natural fruits & veggies are part of what we do.
• Has to convey farm fresh, fresh made and locally made through the design.
• Must have website: www.korvapressery.example
Nice to have
• These can optionally be included on the box:
• - "I care about my health."
• - "Drink Juice. Live Healthier."
• The box can be branded "The Pulp Crate" on 1+ sides

```html
<!DOCTYPE html>
<html lang="en">
<head>
<meta charset="utf-8">
<title>Korva Pressery – Shipping Box Panels</title>
<link rel="stylesheet" href="https://fonts.googleapis.com/css2?family=Caveat:wght@500&family=Open+Sans:wght@400;600&display=swap">
<style>
  :root {
    --kraft: #c8a873;
    --kraft-edge: #b8955d;
    --ink-band: #262626;
    --gold: #d8b983;
    --ink-text: #2b2b2b;
    --page: #ffffff;
    --panel: 280px;
  }
  * { box-sizing: border-box; margin: 0; padding: 0; }
  html, body { width: 1200px; height: 848px; overflow: hidden; background: var(--page); }
  .canvas { position: relative; width: 1200px; height: 848px; }

  .panel {
    position: absolute;
    width: var(--panel);
    height: var(--panel);
    background: var(--kraft);
    outline: 1px solid var(--kraft-edge);
    overflow: hidden;
  }
  .panel--top   { left: 40px;  top: 80px; }
  .panel--front { left: 40px;  top: 360px; }
  .panel--about { left: 320px; top: 360px; }
  .panel--promo { left: 600px; top: 360px; }
  .panel--facts { left: 880px; top: 360px; }

  /* dark band wrapping over top and front */
  .band {
    position: absolute;
    background: var(--ink-band);
    display: flex;
    flex-direction: column;
    align-items: center;
    justify-content: center;
    color: var(--gold);
    text-align: center;
  }
  .band--vertical { left: 34px; right: 34px; top: 0; bottom: 0; }
  .band--horizontal { left: 0; right: 0; top: 34px; bottom: 34px; }

  .brand {
    display: flex;
    align-items: center;
    gap: 6px;
    font-family: "Caveat", cursive;
    font-weight: 500;
    color: var(--gold);
    line-height: 1;
  }
  .brand__dot { width: 9px; height: 9px; border-radius: 50%; background: var(--gold); }
  .brand--large { font-size: 44px; }
  .brand--medium { font-size: 34px; }

  .tagline {
    font-family: "Caveat", cursive;
    font-weight: 500;
    font-size: 25px;
    color: var(--gold);
    margin-top: 14px;
    padding-bottom: 4px;
    border-bottom: 1px solid var(--gold);
  }

  .text-panel {
    position: absolute;
    inset: 0;
    padding: 22px 22px 16px;
    color: var(--ink-text);
    font-family: "Open Sans", sans-serif;
    display: flex;
    flex-direction: column;
  }
  .heading {
    font-family: "Caveat", cursive;
    font-weight: 500;
    font-size: 25px;
    text-align: center;
    line-height: 1.1;
    margin-bottom: 8px;
  }
  .copy { font-size: 8.4px; line-height: 1.55; text-align: justify; }
  .bullets { font-size: 7.8px; line-height: 1.5; padding-left: 12px; margin-bottom: 12px; }
  .web-note { font-size: 7px; text-align: center; margin-top: auto; }

  .features { display: flex; justify-content: space-between; margin-top: 18px; }
  .feature { width: 40px; text-align: center; font-size: 6.5px; line-height: 1.2; }
  .feature svg { display: block; margin: 0 auto 4px; }
</style>
</head>
<body>
<main class="canvas">

  <!-- Top flap -->
  <section class="panel panel--top">
    <div class="band band--horizontal">
      <div class="brand brand--medium"><span class="brand__dot"></span>Korva Pressery</div>
      <p class="tagline">Drink Juice. Live Healthier</p>
    </div>
  </section>

  <!-- Front side -->
  <section class="panel panel--front">
    <div class="band band--vertical">
      <div class="brand brand--large"><span class="brand__dot"></span>Korva<br>Pressery</div>
      <p class="tagline">Drink Juice. Live Healthier</p>
    </div>
  </section>

  <!-- About side -->
  <section class="panel panel--about">
    <div class="text-panel">
      <h2 class="heading">Korva Pressery</h2>
      <p class="copy">Welcome to Korva Pressery, where fresh juice cleanses and juice products are what we do best. We help you transform your day through a balanced approach to nutrition. Start a new healthy routine with our signature juices and keep it going with a weekly subscription delivered right to your door.</p>
      <div class="features">
        <div class="feature">
          <svg width="20" height="20" viewBox="0 0 20 20" fill="none" stroke="currentColor" stroke-width="1.3"><path d="M6 18 L14 2"/><path d="M10 10 L15 8"/></svg>Raw Juice
        </div>
        <div class="feature">
          <svg width="20" height="20" viewBox="0 0 20 20" fill="none" stroke="currentColor" stroke-width="1.3"><circle cx="10" cy="10" r="7"/><path d="M5 15 L15 5"/></svg>Never Heated
        </div>
        <div class="feature">
          <svg width="20" height="20" viewBox="0 0 20 20" fill="none" stroke="currentColor" stroke-width="1.3"><path d="M10 18 C4 11 5 4 10 4 C15 4 16 11 10 18Z"/><circle cx="10" cy="8.5" r="2"/></svg>Locally Grown
        </div>
        <div class="feature">
          <svg width="20" height="20" viewBox="0 0 20 20" fill="none" stroke="currentColor" stroke-width="1.3"><rect x="5" y="6" width="10" height="12"/><path d="M4 3 H16"/></svg>Cold Pressed
        </div>
        <div class="feature">
          <svg width="20" height="20" viewBox="0 0 20 20" fill="none" stroke="currentColor" stroke-width="1.3"><circle cx="10" cy="10" r="7"/><path d="M6.5 10 L9 12.5 L13.5 7.5"/></svg>Plant Based
        </div>
      </div>
      <p class="web-note">Visit our website at www.korvapressery.example</p>
    </div>
  </section>

  <!-- Promo side -->
  <section class="panel panel--promo">
    <div class="band band--vertical">
      <div class="brand brand--large"><span class="brand__dot"></span>Korva<br>Pressery</div>
      <p class="tagline">Be Healthier Without The Hassle</p>
    </div>
  </section>

  <!-- Facts side -->
  <section class="panel panel--facts">
    <div class="text-panel">
      <h2 class="heading">Fresh Ingridients</h2>
      <ul class="bullets">
        <li>Ingredients are locally sourced from family owned farms.</li>
        <li>Fresher produce makes tastier, more nutritious juice.</li>
        <li>Sustainably grown produce helps preserve soil and reduce erosion.</li>
      </ul>
      <h2 class="heading">Convenient Delivery</h2>
      <ul class="bullets">
        <li>All juice is delivered in eco-friendly cold boxes.</li>
        <li>Your juice will remain refrigerated until you get home.</li>
        <li>Shipping notification, so you know exactly when it arrives.</li>
      </ul>
      <p class="web-note">Visit our website at www.korvapressery.example</p>
    </div>
  </section>

</main>
</body>
</html>
```